Billboard for Law Firm

I am looking for a billboard designs. Our branding right now is not good. The logo has to stay the same, but please help come up with something modern, airy, perhaps geometric for the supporting design elements.
Colors should probably be red and blue, or shades of blue, but you can play with the exact shades. Doesn't have to match what you see in the attachment.

The billboard should include:

- Some type of design to bring it to life.

- Logo

- Accident & Injury Law

- 614.300.7000

- Disclaimer (very small text): No Representation Made That The Quality of Legal Services Performed is Greater Than the Those of Other Attorneys

Slogan (very large): Grits, Gravy, and a Good Attorney

______________

Target Market(s)

Southern United States

Industry/Entity Type

Legal Services

Font styles to use
Serif
Sans Serif

Colors
0054AA
0677BA
7BADD7
CADEEF
E8F1F8
EB3D1F
EC4F4E
F09395
F8D3D4
FCEDEE

Requirements
Must have
• Help Make it Memorable and Easy to Read (large text for slogan)
Nice to have
• Some shapes or design elements that may become part of our branding.

```html
<!DOCTYPE html>
<html lang="en">
<head>
<meta charset="utf-8">
<title>Billboard – The Hartwell Firm</title>
<link rel="stylesheet" href="https://fonts.googleapis.com/css2?family=Antonio:wght@400;700&family=Cinzel:wght@500&display=swap">
<style>
  :root {
    --brand-blue: #0149a0;
    --brand-blue-deep: #003f8f;
    --mark-blue: #0677ba;
    --alert-red: #e0070b;
    --ink-black: #050505;
    --paper-white: #ffffff;
    --backdrop: #e8f1f8;
  }
  * { box-sizing: border-box; margin: 0; padding: 0; }
  html, body { width: 1200px; height: 1200px; overflow: hidden; background: var(--backdrop); }
  .billboard {
    position: absolute; left: 40px; top: 435px; width: 1120px; height: 330px;
    background: linear-gradient(100deg, var(--brand-blue-deep), var(--brand-blue));
    overflow: hidden; color: var(--paper-white);
  }
  .slogan {
    position: absolute; left: 36px; top: 26px;
    font-family: "Antonio", "Arial Narrow", sans-serif; font-weight: 700;
    font-size: 122px; line-height: 1.02; text-transform: uppercase; white-space: nowrap;
    transform: scaleX(0.58); transform-origin: left top;
  }
  .disclaimer-band {
    position: absolute; left: 0; bottom: 0; width: 550px; height: 32px;
    background: var(--ink-black); clip-path: polygon(0 0, 100% 0, 97% 100%, 0 100%);
  }
  .disclaimer {
    position: absolute; left: 22px; top: 10px;
    font-family: "Antonio", "Arial Narrow", sans-serif; font-weight: 400;
    font-size: 10px; letter-spacing: 0; text-transform: uppercase; white-space: nowrap;
  }
  .logo-mark {
    position: absolute; left: 580px; top: 46px; width: 110px; height: 110px;
    border-radius: 50%; background: var(--mark-blue);
  }
  .firm-name {
    position: absolute; left: 705px; top: 36px; width: 395px; text-align: center;
    font-family: "Cinzel", Georgia, serif; font-weight: 500;
    font-size: 50px; line-height: 1.1; letter-spacing: 1px;
  }
  .firm-tagline {
    position: absolute; left: 705px; top: 164px; width: 395px; text-align: center;
    font-family: "Cinzel", Georgia, serif; font-weight: 500; font-size: 19px; letter-spacing: 1px;
  }
  .phone-band {
    position: absolute; left: 520px; top: 212px; width: 600px; height: 92px;
    background: var(--alert-red); clip-path: polygon(4% 0, 100% 0, 100% 100%, 0 100%);
    display: flex; align-items: center; padding-left: 44px; gap: 16px;
  }
  .phone-icon { width: 50px; height: 58px; flex: none; }
  .phone-number {
    font-family: "Antonio", "Arial Narrow", sans-serif; font-weight: 700;
    font-size: 88px; line-height: 1; letter-spacing: 2px;
  }
</style>
</head>
<body>
  <section class="billboard">
    <h1 class="slogan">Grits, Gravy, and<br>a Good Attorney</h1>

    <div class="logo-mark" aria-hidden="true"></div>
    <div class="firm-name">The Hartwell<br>Firm</div>
    <div class="firm-tagline">Injury &amp; Accident Lawyers</div>

    <div class="phone-band">
      <svg class="phone-icon" viewBox="0 0 50 58" aria-hidden="true">
        <path d="M10 6 l8 -3 l7 14 l-6 4 q-1 8 6 18 l6 -3 l8 12 l-7 5 q-8 3 -18 -12 q-10 -17 -4 -35 z" fill="var(--paper-white)"/>
        <path d="M30 14 q8 5 8 14" stroke="var(--paper-white)" stroke-width="3" fill="none" stroke-linecap="round"/>
        <path d="M33 7 q12 8 12 22" stroke="var(--paper-white)" stroke-width="3" fill="none" stroke-linecap="round"/>
      </svg>
      <span class="phone-number">614.300.7000</span>
    </div>

    <div class="disclaimer-band">
      <p class="disclaimer">No representation made that the quality of legal services performed is greater than the those of other attorneys</p>
    </div>
  </section>
</body>
</html>
```